Website Design for my Copper Distillation Equipment Business Nature Sciencey Theme

I already have a website www.halvorkettleworks.com and its a pixelhut website builder one. But I cannot get the design right at all. I need this fixed.

I have logo. I need a redesign, for my website, the home page, that maybe I can have something similar in design- I can use as template to copy, for other pages so the whole thing matches? Look at my website so you understand I have a few pages...but most are links. Its a competition. Code has to be easy for me to implement, I am not expert.

Your advice needed..It would be a plus if I can update this myself throughout time. If I could have this explained to me too, the maintenance of it...how would I do this too..etc..pretend I am a child when you explain, if you can. I am not good with this stuff but I am smart and can learn fast.

I want a high end look. Maybe like an ivy league college-y look too, real preppy, chemistry...science-y, nature like is good, leaves, drops water, fields of wheat, lavender, etc.

I want every page to look similar, but the home page is what I want to be the main showpiece,..and I want each page have a little text section, maybe a photos section and a video section, for that market. Like a nice website. If I am not doing this right, let me know. I can work with you. Just help me, please. Let me know if I am doing this right.

When I pick my winning design, for my website, I will hire the artist one-on-one to re-design my shopping cart next. Or if I need additional help with implementing this current design, I can hire the same artist again too. I have a blog that I may want to hire the redesign as well too, but later on. My point is I am not just looking for one project here but I want to follow up with winning artist. So it would be return business for the winner.

I got my logo done here so I am repeat customer. And I have given that winning artist other design work.

Target Market(s)

Moonshine Stills I sell most, Essential Oil Business, Micro and Craft Distilleries, Canna-businesses, Alcohol Fuel

Industry/Entity Type

Business

Number of Pages Required

5+ page

Colors
ec1f27

Requirements
Must have
• The categories for the stills must be prominent and eye catching. The main photo I would like to be naturelike theme, but you can try out different things with me. I am open to ideas and suggestions. I would like this to be implemented easy and fast.
Nice to have
• My logo in it. You can use any of my photos as well from my snapvale account. https://www.snapvale.net/photos/81726354@X07/
• Colors of my Logo...matching design.
• Maybe some basic stock photos you see would match for me..
• Chemistry like symbols for the categories, I love that.

```html
<!DOCTYPE html>
<html lang="en">
<head>
<meta charset="utf-8">
<title>Halvor Kettleworks — Distillation Equipment</title>
<link href="https://fonts.googleapis.com/css2?family=Questrial&family=Great+Vibes&family=Open+Sans:wght@400;600&family=Roboto+Condensed:wght@700&display=swap" rel="stylesheet">
<style>
:root{
  --red-deep:#5e0f10;
  --red-mid:#8a1f1c;
  --red-bright:#a8322b;
  --cream:#ffffff;
  --paper:#f4f4f4;
  --ink:#222222;
  --body-ink:#666666;
  --rule:#c98a86;
  --photo-wood:#6d4a35;
  --photo-green:#3d5a2a;
}
*{box-sizing:border-box;margin:0;padding:0}
html,body{width:1200px;height:2628px;overflow:hidden}
body{position:relative;background:var(--cream);font-family:'Open Sans',sans-serif;color:var(--ink)}

.hero-band{position:absolute;left:0;top:0;width:1200px;height:780px;
  background:radial-gradient(ellipse at 50% 10%,var(--red-bright) 0%,var(--red-mid) 45%,var(--red-deep) 100%)}
.hero-fade{position:absolute;left:0;top:780px;width:1200px;height:160px;
  background:linear-gradient(#e6e6e6,var(--cream))}

.main-nav{position:absolute;top:80px;font-family:'Questrial',sans-serif;font-size:16px;color:#fff;display:flex;gap:38px;text-transform:uppercase}
.main-nav.left{left:96px}
.main-nav.right{left:706px}

.brand{position:absolute;left:0;top:60px;width:1200px;display:flex;justify-content:center;align-items:center;gap:12px}
.brand-dot{width:18px;height:18px;border-radius:50%;background:#fff}
.brand-name{font-family:'Questrial',sans-serif;font-size:26px;color:#fff;letter-spacing:1px}

.tagline{position:absolute;left:0;top:208px;width:1200px;text-align:center;
  font-family:'Great Vibes',cursive;font-size:42px;color:#fff}

.category-bar{position:absolute;left:96px;top:318px;width:1014px;height:62px;display:flex;justify-content:space-between;align-items:flex-start}
.category{font-family:'Roboto Condensed',sans-serif;font-weight:700;font-size:15px;line-height:18px;color:#fff;text-transform:uppercase;text-align:center;padding:12px 8px 0;border-right:1px solid var(--rule);height:62px;flex:1}
.category:last-child{border-right:none}

.slider{position:absolute;left:77px;top:385px;width:1044px;height:480px;border:6px solid #fff;box-shadow:0 30px 40px -20px rgba(0,0,0,.5);
  background:linear-gradient(180deg,var(--photo-green) 0%,#6f8a4c 30%,var(--photo-wood) 55%,#4b3326 100%)}
.slider-dots{position:absolute;left:50%;bottom:14px;transform:translateX(-50%);display:flex;gap:8px}
.slider-dots span{width:10px;height:10px;border-radius:50%;background:rgba(255,255,255,.6)}
.slider-dots span:first-child{background:#fff}

.headline{position:absolute;left:0;top:952px;width:1200px;text-align:center;font-family:'Questrial',sans-serif;font-size:30px;line-height:40px;color:var(--ink);text-transform:uppercase}

.video{position:absolute;left:136px;top:1055px;width:928px;height:434px;
  background:linear-gradient(135deg,#7a5a3a 0%,#a3825c 40%,#3f4b5a 100%)}
.play{position:absolute;left:50%;top:50%;transform:translate(-50%,-50%)}

.intro{position:absolute;left:136px;top:1522px;width:928px;font-size:13px;line-height:22px;color:var(--body-ink)}
.intro p{margin-bottom:22px}

.products{position:absolute;left:72px;top:1960px;width:1056px;display:flex;justify-content:space-between}
.product{width:246px}
.product-photo{height:232px;border:4px solid #fff;box-shadow:0 0 0 1px #ddd}
.product-photo.forest{background:linear-gradient(#3d6b2f,#6f8f4d)}
.product-photo.kitchen{background:linear-gradient(#c9c4bf,#8b7f75)}
.product-photo.porch{background:linear-gradient(#b3a27a,#6a6d53)}
.product-title{margin-top:92px;font-family:'Questrial',sans-serif;font-size:15px;line-height:19px;color:var(--ink);height:38px}
.buy{margin-top:4px;display:inline-block;border:2px solid var(--red-deep);padding:6px 16px;font-family:'Questrial',sans-serif;font-size:13px;color:var(--ink);text-transform:uppercase}

.footer{position:absolute;left:0;top:2431px;width:1200px;height:197px;background:linear-gradient(var(--red-mid),var(--red-deep));color:#fff;font-family:'Questrial',sans-serif}
.footer-contact{position:absolute;top:36px;left:0;width:1200px;display:flex;justify-content:center;align-items:center;gap:40px;font-size:14px}
.footer-brand{font-size:18px}
.footer-nav{position:absolute;top:110px;left:0;width:1200px;display:flex;justify-content:center;gap:22px;font-size:15px;text-transform:uppercase}
.copyright{position:absolute;top:160px;left:0;width:1200px;text-align:center;font-size:12px}
</style>
</head>
<body>
<div class="hero-band"></div>
<div class="hero-fade"></div>

<nav class="main-nav left"><span>Home</span><span>About Us</span><span>Photo Gallery</span><span>Video</span></nav>
<div class="brand"><span class="brand-dot"></span></div>
<nav class="main-nav right"><span>Shop</span><span>Blog</span><span>Books</span><span>Links</span><span>Contact</span></nav>
<div class="brand" style="top:122px"><span class="brand-name">Halvor Kettleworks</span></div>

<div class="tagline">Please Choose the Category of the Still you are looking for...</div>

<div class="category-bar">
  <div class="category">Stills</div>
  <div class="category">Essential<br>Oils</div>
  <div class="category">Alcohol<br>Fuel</div>
  <div class="category">Cannabis</div>
  <div class="category">Boilers</div>
  <div class="category">Home<br>Distillers</div>
  <div class="category">Vodka<br>Still</div>
  <div class="category">Heat<br>Control</div>
  <div class="category">Distillery</div>
  <div class="category">Kits</div>
  <div class="category">Parts</div>
</div>

<div class="slider" role="img" aria-label="Copper still and glass jar with oranges on an outdoor wooden deck table among trees">
  <div class="slider-dots"><span></span><span></span><span></span></div>
</div>

<h1 class="headline">Purity comes from<br>a direct connection with nature...</h1>

<div class="video" role="img" aria-label="Video still: herbal extraction demonstration in a kitchen with a blender">
  <svg class="play" width="64" height="64" viewBox="0 0 64 64"><circle cx="32" cy="32" r="30" fill="rgba(255,255,255,.85)"/><circle cx="32" cy="32" r="26" fill="none" stroke="#333" stroke-width="2"/><path d="M26 20 L46 32 L26 44 Z" fill="#333"/></svg>
</div>

<div class="intro">
  <p>Welcome to our Website. Are you looking for a Moonshine Still? Are you a Lavender Farm? Are you wanting to distill Essential Oils on your farm and make Hydrosols too? Do you want to make an Herbal Extraction or Tincture? Do you want to start a Home Business? Are you a Micro (small) Distillery wanting a Set up? Are you a Race Car driver looking for alternative ways to get your Ethanol? Are you a Prepper? Are you interested in Making Alcohol in times of Survival? Do you need clean radiation free Water for your community? Do you want to support Local Farmers, get back to the Source and Nature? Are you a Canna-business or 502?</p>
  <p>My Dream Customer is someone who believes they cannot, but does it anyways and finds out they can! And then they go and teach someone....that is a gift that keeps on giving. Those are the results I want to give. Taking a liquid, turning it into a vapor and then back into a liquid. That is all you need to know.</p>
  <p>To Purchase a Still, you can browse through our Cart. We have How To Articles in our Blog, and in the Links section, also watch step by step Videos and see detailed Photos of all our products. Read our manuals. See our tests results. See me on tv and in magazine articles. I have a weekly Live StreamLoft as well, if you want to interact with questions. I can give you projects. We have TalkDock and MeetNook.</p>
  <p>Please ask us questions. Call us for a free quote. We sell Distillation Equipment and we can customize your projects. We ship Alcohol Stills all around the world, we are an online only store.</p>
</div>

<div class="products">
  <div class="product">
    <div class="product-photo forest" role="img" aria-label="Copper still tower on a keg outdoors among trees"></div>
    <div class="product-title">Copper Still -3 Inch-Tower only</div>
    <span class="buy">Buy</span>
  </div>
  <div class="product">
    <div class="product-photo forest" role="img" aria-label="Essential oil distiller in a garden"></div>
    <div class="product-title">Essential Oil Distiller</div>
    <span class="buy">Buy</span>
  </div>
  <div class="product">
    <div class="product-photo kitchen" role="img" aria-label="Copper still on a 15 gallon keg indoors"></div>
    <div class="product-title">Copper Still- with NON ELECTRIC 15 Gallon Keg</div>
    <span class="buy">Buy</span>
  </div>
  <div class="product">
    <div class="product-photo porch" role="img" aria-label="Complete ethanol distilling kit on a porch"></div>
    <div class="product-title">Distilling Alcohol Ethanol Complete Kit 3 Inch</div>
    <span class="buy">Buy</span>
  </div>
</div>

<footer class="footer">
  <div class="footer-contact">
    <span>+1 555 014 2290</span>
    <span class="footer-brand">Halvor Kettleworks</span>
    <span>info@halvorkettleworks.com</span>
  </div>
  <nav class="footer-nav"><span>Home</span><span>About Us</span><span>Photogallery</span><span>Video</span><span>Shop</span><span>Blog</span><span>Books</span><span>Links</span><span>Contact Us</span></nav>
  <div class="copyright">© 2015 Halvor Kettleworks - All Rights Reserved</div>
</footer>
</body>
</html>
```